Business card design for Allied Healthcare provider

We would like a design for front and back of business cards. The design must resonate with all levels of customers from patients, to other health providers and medical. Must also resonate with corporate customers

Target Market(s)

patients, medical practitioners, other health providers and corporate.

Industry/Entity Type

healthcare

Contact Information for Business Card

name, logo, phone and fax numbers, email, website

Requirements
Must have
• not allowing me to change this, but the card must be double sided!! Please take note
Nice to have
• a fresh yet bold design to catch attention.

```html
<!DOCTYPE html>
<html lang="en">
<head>
<meta charset="utf-8">
<title>vitalcrest business card</title>
<link href="https://fonts.googleapis.com/css2?family=Lexend:wght@400;500&family=Raleway:wght@600&family=Arimo:wght@400&display=swap" rel="stylesheet">
<style>
  :root {
    --navy: #1b2d57;
    --gold: #fbb726;
    --white: #ffffff;
    --backdrop: #e1dfdf;
  }
  html, body {
    margin: 0;
    padding: 0;
    overflow: hidden;
  }
  .canvas {
    position: relative;
    width: 1075px;
    height: 1200px;
    background: var(--backdrop);
    overflow: hidden;
  }
  .card {
    position: absolute;
    border-radius: 22px;
    overflow: hidden;
  }
  .card-front {
    left: 206px;
    top: 166px;
    width: 667px;
    height: 397px;
    background: var(--navy);
    display: flex;
    align-items: center;
    justify-content: center;
  }
  .brand {
    display: flex;
    align-items: center;
    gap: 16px;
    font-family: "Lexend", sans-serif;
    font-weight: 500;
    letter-spacing: -0.5px;
    line-height: 1;
  }
  .brand-dot {
    border-radius: 50%;
    flex: none;
  }
  .card-front .brand {
    font-size: 52px;
    color: var(--white);
    transform: translateY(-20px);
  }
  .card-front .brand-dot {
    width: 62px;
    height: 62px;
    background: var(--gold);
  }
  .card-back {
    left: 211px;
    top: 638px;
    width: 659px;
    height: 396px;
    background: var(--white);
  }
  .card-back .brand {
    position: absolute;
    left: 212px;
    top: 90px;
    font-size: 50px;
    color: var(--navy);
  }
  .card-back .brand-dot {
    width: 64px;
    height: 64px;
    background: var(--navy);
  }
  .tagline {
    position: absolute;
    left: 303px;
    top: 146px;
    font-family: "Lexend", sans-serif;
    font-weight: 400;
    font-size: 18px;
    line-height: 22px;
    color: var(--gold);
    word-spacing: 2px;
  }
  .holder {
    position: absolute;
    left: 32px;
    top: 200px;
  }
  .holder-name {
    font-family: "Raleway", sans-serif;
    font-weight: 600;
    font-size: 30px;
    color: var(--gold);
    line-height: 36px;
  }
  .holder-role {
    font-family: "Arimo", sans-serif;
    font-size: 18px;
    color: var(--navy);
    line-height: 22px;
  }
  .rule {
    position: absolute;
    left: 32px;
    top: 274px;
    width: 220px;
    height: 5px;
    background: var(--gold);
  }
  .contact-band {
    position: absolute;
    left: 0;
    right: 0;
    top: 279px;
    bottom: 0;
    background: var(--navy);
    font-family: "Arimo", sans-serif;
    font-size: 18px;
    color: var(--white);
  }
  .contact-list {
    position: absolute;
    top: 34px;
    margin: 0;
    padding: 0;
    list-style: none;
  }
  .contact-list li {
    display: flex;
    align-items: center;
    gap: 8px;
    height: 24px;
  }
  .contact-list.left { left: 32px; }
  .contact-list.right { right: 48px; }
  .contact-list.right li { justify-content: flex-end; }
  .icon { width: 18px; height: 18px; flex: none; }
  .accent { color: var(--gold); }
</style>
</head>
<body>
<div class="canvas">

  <section class="card card-front">
    <div class="brand"><span class="brand-dot"></span>vitalcrest</div>
  </section>

  <section class="card card-back">
    <div class="brand"><span class="brand-dot"></span>vitalcrest</div>
    <div class="tagline">care • guidance • wellness</div>

    <div class="holder">
      <div class="holder-name">Daniel Morgan</div>
      <div class="holder-role">Managing Director</div>
    </div>
    <div class="rule"></div>

    <div class="contact-band">
      <ul class="contact-list left">
        <li>
          <svg class="icon" viewBox="0 0 24 24" aria-hidden="true"><path fill="#fbb726" d="M6.6 10.8a15.1 15.1 0 0 0 6.6 6.6l2.2-2.2c.3-.3.7-.4 1-.2 1.1.4 2.3.6 3.6.6.6 0 1 .4 1 1V20c0 .6-.4 1-1 1A17 17 0 0 1 3 4c0-.6.4-1 1-1h3.5c.6 0 1 .4 1 1 0 1.3.2 2.5.6 3.6.1.3 0 .7-.2 1z"/></svg>
          055-210 384 617
        </li>
        <li>
          <svg class="icon" viewBox="0 0 24 24" aria-hidden="true"><path fill="#fbb726" d="M6 2h9l3 3v4H6zM3 10h18a1 1 0 0 1 1 1v7h-4v4H6v-4H2v-7a1 1 0 0 1 1-1zm5 6v4h8v-4z"/></svg>
          055-210 384 618
        </li>
      </ul>
      <ul class="contact-list right">
        <li>
          info@sitename.com
          <svg class="icon" viewBox="0 0 24 24" aria-hidden="true"><rect x="2" y="5" width="20" height="14" fill="#fbb726"/><path d="M2 5l10 8 10-8" fill="none" stroke="#1b2d57" stroke-width="1.8"/></svg>
        </li>
        <li>
          <span>www.<span class="accent">sitename</span>.com</span>
          <svg class="icon" viewBox="0 0 24 24" aria-hidden="true"><g fill="none" stroke="#fbb726" stroke-width="2"><circle cx="12" cy="12" r="9"/><ellipse cx="12" cy="12" rx="4" ry="9"/><path d="M3 12h18M5 7.5h14M5 16.5h14"/></g></svg>
        </li>
      </ul>
    </div>
  </section>

</div>
</body>
</html>
```